Infographic that describes our service

We want to clearly explain what we offer. VOM (our company) is unique. Our members watch videos that include a real person who struggles with mental health and a clinician who analyzes their condition. The clinician breaks down the issues for our subscribers and the clinicians provides advice and coping skills that our members can apply to their own situation. The infographic must not be long/complex. It must be simple, must be a square, and must be understood in 5 second by the reader.

To better understand VOM... here's what we're not:
- online therapy
- a mental health documentary video website
- group therapy

What VOM is...
- our subscribers watch other people share their experience
- our clinicians analyze other people (not the subscriber) and breakdown those experiences so that our subscribers can learn what to do if they suffer from the same issue
- our subscribers get advice and coping skills from clinicians

Target Market(s)

People who suffer from mental health issues

Industry/Entity Type

Mental health

Requirements
Must have
• See www.seevom.tv and use our creative look and feel. Must watch our intro video on the home page to understand our service.
Nice to have
• Here is some additional language you are free to use whatever parts work best for your design... Welcome to VOM. Where real people share their struggles with you and experts analyze those struggles to give you advice and coping skills. From anxiety to depression and many more conditions, we’ve got covered. Simply browse the topics and watch. It’s a new way to heal.
Should not have
• Please don't include the website URL on the infographic - this graphic will be used on our home page, not as a standalone infographic. Please don't include a visual of a patient and therapist together on the screen at the same time. VOM works by having a person record themself, then a therapist reviews that recording and analyzes it for our subscribers. Thanks!

```html
<!DOCTYPE html>
<html lang="en">
<head>
<meta charset="utf-8">
<title>VOM – Heal in a Brand New Way</title>
<link rel="stylesheet" href="https://fonts.googleapis.com/css2?family=Montserrat:wght@400;500;700;800&display=swap">
<style>
  :root {
    --orange: #ef7d35;
    --blue-dark: #266b8f;
    --blue-deep: #1b5783;
    --blue-light: #93bfd6;
    --blue-pale: #cde0ea;
    --mist: #e9eef3;
    --grey-label: #c3c3c6;
    --white: #ffffff;
  }
  html, body {
    margin: 0;
    padding: 0;
    width: 1200px;
    height: 1200px;
    overflow: hidden;
    background: var(--white);
  }
  .infographic {
    position: relative;
    width: 1200px;
    height: 1200px;
    overflow: hidden;
    font-family: "Montserrat", Arial, sans-serif;
    background: var(--white);
  }
  .artwork {
    position: absolute;
    inset: 0;
  }
  .hero-copy {
    position: absolute;
    left: 0;
    top: 0;
    width: 1200px;
    text-align: center;
    color: var(--white);
  }
  .hero-title {
    position: absolute;
    left: 0;
    right: 0;
    top: 66px;
    margin: 0;
    font-weight: 800;
    font-size: 53px;
    letter-spacing: 0;
    line-height: 1;
    padding-left: 0;
  }
  .hero-intro {
    position: absolute;
    left: 150px;
    width: 900px;
    top: 139px;
    margin: 0;
    font-weight: 500;
    font-size: 24px;
    line-height: 31px;
  }
  .hero-cta {
    position: absolute;
    left: 0;
    right: 0;
    top: 246px;
    margin: 0;
    font-weight: 500;
    font-size: 24px;
  }
  .hero-cta strong {
    font-weight: 800;
    text-decoration: underline;
    text-underline-offset: 3px;
  }
  .step-label {
    position: absolute;
    margin: 0;
    font-weight: 500;
    font-size: 20px;
    line-height: 24px;
  }
  .step-label--record {
    left: 400px;
    width: 384px;
    top: 346px;
    text-align: center;
    color: var(--blue-light);
  }
  .step-label--watch {
    right: 933px;
    width: 260px;
    top: 900px;
    text-align: right;
    color: var(--blue-dark);
  }
  .step-label--review {
    left: 917px;
    width: 260px;
    top: 900px;
    color: var(--orange);
  }
  .brand-name {
    position: absolute;
    left: 917px;
    top: 962px;
    margin: 0;
    color: var(--orange);
    font-weight: 700;
    font-size: 22px;
    line-height: 28px;
  }
  .flow-text {
    font-family: "Montserrat", Arial, sans-serif;
    font-weight: 800;
    font-size: 26px;
    letter-spacing: 1px;
    fill: var(--grey-label);
  }
  .flow-arc { fill: none; stroke-width: 4; stroke-dasharray: 2 4; }
  .icon-line { fill: none; stroke: var(--white); stroke-width: 1.6; stroke-linecap: round; stroke-linejoin: round; }
</style>
</head>
<body>
<main class="infographic">
  <svg class="artwork" width="1200" height="1200" viewBox="0 0 1200 1200" xmlns="http://www.w3.org/2000/svg">
    <defs>
      <clipPath id="header-clip"><rect x="0" y="0" width="1200" height="308"/></clipPath>
      <clipPath id="tl-clip"><circle cx="43" cy="31" r="143"/></clipPath>
      <clipPath id="tr-clip"><circle cx="1130" cy="25" r="130"/></clipPath>
      <radialGradient id="photo-tone" cx="50%" cy="40%" r="60%">
        <stop offset="0%" stop-color="#e0b48f"/>
        <stop offset="55%" stop-color="#c99a76"/>
        <stop offset="100%" stop-color="#5a4636"/>
      </radialGradient>
      <path id="ring-path-cw" d="M592,438 A318,318 0 1 1 591.9,438"/>
      <path id="ring-path-bottom" d="M246,756 A346,346 0 0 0 938,756"/>
    </defs>

    <g class="header-band" clip-path="url(#header-clip)">
      <rect x="0" y="0" width="1200" height="308" fill="var(--orange)"/>
      <circle cx="43" cy="31" r="143" fill="var(--blue-light)"/>
      <circle cx="43" cy="273" r="146" fill="var(--blue-dark)"/>
      <circle cx="43" cy="273" r="146" fill="var(--blue-deep)" clip-path="url(#tl-clip)"/>
      <circle cx="1180" cy="248" r="127" fill="var(--blue-light)"/>
      <circle cx="1130" cy="25" r="130" fill="var(--blue-dark)"/>
      <circle cx="1180" cy="248" r="127" fill="var(--blue-deep)" clip-path="url(#tr-clip)"/>
    </g>

    <circle cx="37" cy="1199" r="199" fill="var(--mist)"/>
    <path d="M1174,1174 L1004,1174 A170,170 0 0 1 1174,1004 Z" fill="var(--blue-pale)"/>

    <g class="process-ring" fill="none" stroke-width="33">
      <path d="M412,652 A207.5,207.5 0 0 1 768,646" stroke="var(--blue-light)"/>
      <path d="M768,646 A207.5,207.5 0 0 1 592,963.5" stroke="var(--orange)"/>
      <path d="M592,963.5 A207.5,207.5 0 0 1 412,652" stroke="var(--blue-dark)"/>
    </g>
    <circle cx="592" cy="756" r="176" fill="url(#photo-tone)" role="img" aria-label="Photo of a young woman lying in bed, watching a video on her phone"/>

    <path class="flow-arc" d="M659,466 A298,298 0 0 1 888,787" stroke="var(--blue-light)"/>
    <polygon points="873,814 897,817 874,857" fill="var(--blue-light)"/>
    <path class="flow-arc" d="M795,974 A298,298 0 0 1 393,977" stroke="var(--orange)"/>
    <polygon points="386,972 428,994 407,1009" fill="var(--orange)"/>
    <path class="flow-arc" d="M312,858 A298,298 0 0 1 481,484" stroke="var(--blue-dark)"/>
    <polygon points="524,465 480,472 486,493" fill="var(--blue-dark)"/>

    <text class="flow-text"><textPath href="#ring-path-cw" startOffset="15.4%" text-anchor="middle">VIDEO SHARED WITH EXPERTS</textPath></text>
    <text class="flow-text"><textPath href="#ring-path-cw" startOffset="81.8%" text-anchor="middle">SUBSCRIBERS GET THE ADVICE</textPath></text>
    <text class="flow-text"><textPath href="#ring-path-bottom" startOffset="50.5%" text-anchor="middle">REVIEWS &amp; ANALYSIS UPLOADED</textPath></text>

    <g class="step-icon step-icon--record">
      <circle cx="592" cy="458" r="48" fill="var(--blue-light)"/>
      <rect class="icon-line" x="572" y="426" width="40" height="63" rx="4"/>
      <line class="icon-line" x1="572" y1="434" x2="612" y2="434"/>
      <line class="icon-line" x1="572" y1="480" x2="612" y2="480"/>
      <line class="icon-line" x1="588" y1="430" x2="596" y2="430"/>
      <circle class="icon-line" cx="592" cy="484.5" r="2"/>
      <circle class="icon-line" cx="592" cy="455" r="11.5"/>
      <path class="icon-line" d="M588,449 L598,455 L588,461 Z"/>
    </g>

    <g class="step-icon step-icon--watch">
      <circle cx="341" cy="920" r="48" fill="var(--blue-dark)"/>
      <path class="icon-line" d="M349,923 L315,923 L315,898 L356,898 L356,907" stroke-width="2.4"/>
      <path d="M330,904 L342,911 L330,918 Z" fill="none" stroke="var(--white)" stroke-width="2"/>
      <circle cx="353" cy="918" r="8" fill="var(--white)"/>
      <path d="M337,943 Q338,927 353,927 Q368,927 369,943 Z" fill="var(--white)"/>
    </g>

    <g class="step-icon step-icon--review">
      <circle cx="843" cy="920" r="48" fill="var(--orange)"/>
      <circle class="icon-line" cx="851" cy="913" r="21"/>
      <circle class="icon-line" cx="851" cy="913" r="17"/>
      <path class="icon-line" d="M837,925 L821,943 L825,947 L841,929"/>
      <polyline class="icon-line" points="840,918 846,910 853,916 861,906"/>
      <circle cx="840" cy="918" r="1.8" fill="var(--white)"/>
      <circle cx="846" cy="910" r="1.8" fill="var(--white)"/>
      <circle cx="853" cy="916" r="1.8" fill="var(--white)"/>
      <circle cx="861" cy="906" r="1.8" fill="var(--white)"/>
    </g>
  </svg>

  <header class="hero-copy">
    <h1 class="hero-title">HEAL IN A BRAND NEW WAY</h1>
    <p class="hero-intro">Where real people share their struggles with you and experts analyze those struggles to give you advice and coping skills. From anxiety to depression and many more conditions, we’ve got covered.</p>
    <p class="hero-cta">Simply <strong>BROWSE</strong> the topics and <strong>WATCH</strong>.</p>
  </header>

  <p class="step-label step-label--record">Real patients records<br>themselves</p>
  <p class="step-label step-label--watch">Subscribers watch analysis and reviews under various topics</p>
  <p class="step-label step-label--review">Therapist reviews and analyzes recordings</p>
  <p class="brand-name">VOM</p>
</main>
</body>
</html>
```